Design some Business Card for shipping company

We need a creative business card designed for a shipping company. All relevant information such as address and phone number can be found on our website. Will need a design for both front and back. The front will container our logo, slogan, contact information etc. The back will have a coupon and some text. check out www.talvorfreight.example for all the information. We need something memorable and unique that will stand out. It needs to a horizontal design. Not vertical.

```html
<!DOCTYPE html>
<html lang="en">
<head>
<meta charset="utf-8">
<title>Talvor Freight Business Card</title>
<link href="https://fonts.googleapis.com/css2?family=Fira+Sans:ital,wght@0,400;0,600;0,800;1,400&display=swap" rel="stylesheet">
<style>
  :root {
    --bg: #000000;
    --card: #ffffff;
    --green: #1f7a3c;
    --red: #c8202c;
    --ink: #222222;
    --muted: #555555;
    --faint: #f1f1f1;
  }
  * { box-sizing: border-box; margin: 0; padding: 0; }
  html, body { width: 1200px; height: 675px; overflow: hidden; background: var(--bg); }
  body { position: relative; font-family: "Fira Sans", Arial, sans-serif; color: var(--ink); }

  .card {
    position: absolute;
    top: 178px;
    width: 540px;
    height: 320px;
    background: var(--card);
    border-radius: 16px;
    overflow: hidden;
  }
  .card--contact { left: 40px; }
  .card--brand { left: 620px; }

  /* brand lockup */
  .brand { display: flex; align-items: center; gap: 10px; }
  .brand__dot { width: 34px; height: 34px; border-radius: 50%; background: var(--green); flex: none; }
  .brand__name { font-weight: 800; color: var(--green); font-variant: small-caps; letter-spacing: 0.5px; line-height: 1; white-space: nowrap; }
  .brand__tagline { font-weight: 800; color: var(--ink); line-height: 1.1; white-space: nowrap; }

  /* contact side */
  .card--contact .brand { position: absolute; left: 26px; top: 22px; }
  .card--contact .brand__name { font-size: 26px; }
  .card--contact .brand__tagline { position: absolute; left: 70px; top: 52px; font-size: 13px; }
  .contact-list { position: absolute; left: 28px; top: 112px; list-style: none; font-size: 12px; color: var(--muted); }
  .contact-list li { display: flex; align-items: center; gap: 6px; height: 17px; }
  .contact-list svg { width: 10px; height: 10px; flex: none; }
  .person { position: absolute; right: 34px; top: 162px; text-align: right; }
  .person__name { font-size: 15px; font-weight: 600; letter-spacing: 0.5px; text-transform: uppercase; }
  .person__role { font-size: 12px; color: var(--green); margin-bottom: 8px; }
  .person__address { font-style: normal; font-size: 12px; color: var(--muted); line-height: 1.45; }
  .wave { position: absolute; left: 0; bottom: 0; width: 540px; height: 150px; }

  /* brand side */
  .card--brand .brand { position: absolute; left: 70px; top: 108px; gap: 14px; }
  .card--brand .brand__dot { width: 56px; height: 56px; }
  .card--brand .brand__name { font-size: 40px; }
  .card--brand .brand__tagline { position: absolute; left: 140px; top: 158px; font-size: 18px; }
  .site { position: absolute; left: 0; right: 0; top: 248px; text-align: center; font-size: 13px; letter-spacing: 3px; color: var(--red); }
</style>
</head>
<body>

<section class="card card--contact">
  <div class="brand">
    <span class="brand__dot" aria-hidden="true"></span>
    <span class="brand__name">Talvor Freight</span>
  </div>
  <p class="brand__tagline">Safe Low-Cost Cargo Runs to Nairobi</p>

  <ul class="contact-list">
    <li><svg viewBox="0 0 10 10"><rect x="1" y="1" width="8" height="8" rx="1" fill="none" stroke="#555" stroke-width="1.2"/></svg>+254700418263</li>
    <li><svg viewBox="0 0 10 10"><rect x="0" y="0" width="10" height="10" rx="1.5" fill="#555"/><path d="M3 2h2v2H3.8a4 4 0 0 0 2.2 2.2V5h2v2H7A5 5 0 0 1 3 3z" fill="#fff"/></svg>0700418263</li>
    <li><svg viewBox="0 0 10 10"><rect x="0" y="1.5" width="10" height="7" rx="1" fill="#555"/><path d="M0.5 2l4.5 3.5L9.5 2" fill="none" stroke="#fff" stroke-width="1"/></svg>info@talvorfreight.example</li>
    <li><svg viewBox="0 0 10 10"><circle cx="5" cy="5" r="4.5" fill="#555"/><path d="M0.5 5h9M5 .5c-2 2.5-2 6.5 0 9M5 .5c2 2.5 2 6.5 0 9" fill="none" stroke="#fff" stroke-width="0.7"/></svg>www.talvorfreight.example</li>
  </ul>

  <div class="person">
    <p class="person__name">Daren Holloway</p>
    <p class="person__role">Managing Director</p>
    <address class="person__address">1184 Harbor Ridge Ave NE<br>Suite #214<br>Lakemont WA 98031</address>
  </div>

  <svg class="wave" viewBox="0 0 540 150" preserveAspectRatio="none" aria-hidden="true">
    <path d="M0 30 C120 30 200 80 300 120 C360 142 420 150 540 150 L0 150 Z" fill="var(--red)"/>
    <path d="M0 40 C120 40 200 88 300 126 C350 144 400 150 460 150 L0 150 Z" fill="#ffffff"/>
    <path d="M0 48 C120 48 200 94 290 130 C330 146 370 150 410 150 L0 150 Z" fill="var(--green)"/>
    <path d="M0 138 C60 140 120 146 160 150 L0 150 Z" fill="var(--red)"/>
  </svg>
</section>

<section class="card card--brand">
  <div class="brand">
    <span class="brand__dot" aria-hidden="true"></span>
    <span class="brand__name">Talvor Freight</span>
  </div>
  <p class="brand__tagline">Safe Low-Cost Cargo Runs to Nairobi</p>
  <p class="site">www.talvorfreight.example</p>
</section>

</body>
</html>
```